Live Webcasting Host Wants Template/Theme to Jumpstare Ecommerce Site

Please,Please, Please READ ALL OF THE DESCRIPTION. Thank you.

I need a template for a look for my developer to work with in designing an ecommerce site where clients pay a monthly fee for streaming services and video on demand.

I'll need 2 pages designed:
1) public page
2) client log in landing page.

Please use a CMS (WP preferred) as this will allow is for further content to be added after delivery. Please include the pricing text in boxes in slides (pdf) to help fill out you design for the home page.

The attached slides are to give you a general layout of how I envision the pages. Yes I would like the Client page to be tabbed from the side like in the attached slide.

I've attached company logos for use along with the accompanying .psd and .ai files in the zip. Use the colors in logo in site design.

Thank you for your time.
Updates

Please, no designs. This is for a CMS for webpage design like WordPress or Joomla. Thanks. Added Friday, January 13, 2017

Reason: Looking for more designs.

Target Market(s)

Churches, Organizations, Civic Organizations, Government Agencies (State, Local) -BUT don't let this deter your creativity. Decision makers/influencers will be video production and/or IT personnel.

Industry/Entity Type

It Company

Font styles to use
Sans Serif

Colors
f5f5f5
e8e8e8
333333
fece3e
cbcbcb
33a6d7
000000

Requirements
Must have
• Responsive Design
Nice to have
• One Page Design
Should not have
• SHOULD NOT HAVE White overall background but use white in other ways if you like.

```html
<!DOCTYPE html>
<html lang="en">
<head>
<meta charset="utf-8">
<title>Vireo Streaming</title>
<link href="https://fonts.googleapis.com/css2?family=Anton&family=Lato:wght@300;400;700;900&family=Montserrat:wght@600&family=Roboto+Condensed:wght@700&display=swap" rel="stylesheet">
<style>
:root{
  --yellow:#fece3e;
  --gold:#f7c325;
  --dark:#333333;
  --night:#2a2d33;
  --ink:#000000;
  --light:#f5f5f5;
  --line:#e8e8e8;
  --grey:#cbcbcb;
  --orange:#f7a11a;
  --red:#c8141c;
}
*{margin:0;padding:0;box-sizing:border-box}
html,body{width:724px;height:1200px;overflow:hidden}
body{position:relative;font-family:'Lato',sans-serif;background:#fff;color:var(--dark)}
.abs{position:absolute}

/* hero */
.hero{left:0;top:0;width:724px;height:388px;
  background:radial-gradient(ellipse at 70% 30%,#5d6470 0%,#3a3d42 45%,#1d1d1f 100%)}
.hero-photo{left:0;top:0;width:724px;height:388px;
  background:linear-gradient(160deg,rgba(120,130,145,.55) 0%,rgba(70,62,45,.35) 55%,rgba(150,110,40,.45) 100%)}
.brand{display:flex;align-items:center;font-family:'Lato',sans-serif;font-weight:400;font-size:26px;letter-spacing:1px}
.brand-mark{width:14px;height:14px;background:var(--yellow);margin-right:9px}
.brand-top{left:70px;top:20px;color:#fff}
.brand-foot{left:56px;top:1146px;color:var(--dark)}
.nav{top:54px;left:272px;display:flex;align-items:center;color:#fff;font-size:9.5px}
.nav a{color:#fff;text-decoration:none;margin-left:24px}
.login{left:565px;top:13px;width:87px;height:26px;background:var(--ink);border-radius:13px;
  color:#fff;font-family:'Montserrat',sans-serif;font-weight:600;font-size:12px;letter-spacing:.5px;display:flex;align-items:center}
.login-icon{width:26px;height:26px;border-radius:5px;background:var(--orange);margin-right:8px;display:flex;align-items:center;justify-content:center}
.headline{left:0;top:212px;width:724px;text-align:center;color:#fff;font-family:'Montserrat',sans-serif;font-weight:600;
  font-size:19px;line-height:26.5px;letter-spacing:1.3px}
.cta{left:296px;top:303px;width:126px;height:28px;background:var(--gold);border:2px solid #e8a80f;border-radius:14px;
  font-family:'Roboto Condensed',sans-serif;font-weight:700;font-size:16px;letter-spacing:1px;color:#3a2a05;text-align:center;line-height:24px}

/* pricing */
.pricing{left:0;top:388px;width:724px;height:414px;background:var(--night)}
.pricing-title{left:0;top:438px;width:724px;text-align:center;color:#fff;font-size:20px;letter-spacing:2.4px;font-weight:400}
.card{border-radius:7px;text-align:center;box-shadow:0 3px 6px rgba(0,0,0,.45)}
.card .band{position:absolute;left:0;width:100%}
.card .name{position:absolute;left:0;width:100%;font-family:'Anton',sans-serif;letter-spacing:3px}
.card .price{position:absolute;right:-2px;background:var(--gold);border-radius:14px 0 0 14px;
  font-family:'Anton',sans-serif;color:var(--red);letter-spacing:1px;text-align:center}
.card .info{position:absolute;left:0;width:100%;font-size:9.5px;letter-spacing:1px;line-height:11.5px;color:var(--dark)}
.card .more{position:absolute;background:var(--gold);border:2px solid #e0a40c;border-radius:13px;
  font-family:'Roboto Condensed',sans-serif;font-weight:700;font-size:14px;letter-spacing:1px;color:var(--ink);line-height:20px}
.small{left:53px;top:506px;width:191px;height:222px;background:linear-gradient(180deg,#8fc41b 0%,#b5dc2c 60%,#cfe84a 100%)}
.small .band{background:rgba(255,255,255,.18)}
.small .name{color:#2f3d0c}
.medium{left:255px;top:486px;width:217px;height:260px;background:linear-gradient(180deg,#d8a824 0%,#c99a20 55%,#e3b52c 100%)}
.medium .band{background:rgba(255,255,255,.14)}
.medium .name{color:#f6e321}
.large{left:482px;top:506px;width:192px;height:222px;background:linear-gradient(180deg,#2fb6bd 0%,#4ecfd3 60%,#6ee0e0 100%)}
.large .band{background:rgba(255,255,255,.2)}
.large .name{color:#145b63}

/* about */
.hello{left:56px;top:845px;font-size:26px;letter-spacing:2.4px;color:var(--yellow);font-weight:400}
.welcome{left:56px;top:882px;font-size:12px;letter-spacing:1px;font-weight:400}
.lead{left:55px;top:915px;font-size:10.5px;letter-spacing:.6px;font-weight:400}
.body-copy{left:56px;top:937px;width:362px;font-size:7.4px;line-height:13.5px;color:#a8a8a8}
.testi-title{left:427px;top:845px;font-size:24px;letter-spacing:2.4px;color:var(--ink);font-weight:400}
.testi{top:890px;width:120px}
.avatar{position:absolute;left:0;top:3px;width:37px;height:37px;border-radius:50%;background:linear-gradient(160deg,#d8c0a4,#8a7a6a)}
.who{position:absolute;left:46px;top:1px;font-size:11px;letter-spacing:.8px;color:var(--ink)}
.quote{position:absolute;left:46px;top:18px;width:74px;font-size:7px;line-height:13.5px;color:#b0b0b0}
.quote-long{position:absolute;left:0;top:56px;width:120px;font-size:7px;line-height:13.5px;color:#b0b0b0}

/* newsletter */
.news{left:0;top:1048px;width:724px;height:70px;background:var(--line)}
.news-label{left:118px;top:1076px;font-size:10.5px;letter-spacing:.3px;display:flex;align-items:center;white-space:nowrap}
.news-label svg{margin-right:9px}
.email{left:326px;top:1069px;width:200px;height:26px;background:#fff;font-size:6.5px;color:var(--grey);padding:10px 3px}
.subscribe{left:536px;top:1069px;width:74px;height:26px;background:var(--orange);color:var(--dark);font-size:10px;text-align:center;line-height:26px;letter-spacing:.5px}

/* footer */
.copy{left:187px;top:1159px;font-size:11px;letter-spacing:.5px}
.social{top:1155px;width:20px;height:20px;border-radius:50%;background:var(--dark)}
.to-top{left:674px;top:1175px;width:25px;height:25px;background:var(--orange);display:flex;align-items:center;justify-content:center}
</style>
</head>
<body>

<section class="abs hero"></section>
<div class="abs hero-photo" role="img" aria-label="Blurred photo of a broadcast audio mixing console"></div>

<div class="abs brand brand-top"><span class="brand-mark"></span>Vireo</div>

<nav class="abs nav">
  <svg width="20" height="18" viewBox="0 0 20 18"><path d="M10 1 L19 9 H16 V17 H12 V12 H8 V17 H4 V9 H1 Z" fill="#f7a11a"/></svg>
  <a>FEATURES</a><a>PRICING</a><a>ABOUT US</a><a>WEBCASTING 101</a><a>CONTACT</a>
</nav>

<div class="abs login">
  <span class="login-icon"><svg width="16" height="16" viewBox="0 0 16 16"><circle cx="7" cy="5" r="3.5" fill="#222"/><path d="M1 15 C1 10 13 10 13 15 Z" fill="#222"/></svg></span>LOGIN
</div>

<h1 class="abs headline">YOU CAN EASILY PAY A MONTHLY FEE<br>FOR STREAMING SERVICES AND<br>VIDEO ON DEMAND</h1>
<div class="abs cta">Get Started</div>

<section class="abs pricing"></section>
<h2 class="abs pricing-title">OUR PRICING &amp; PACKAGES</h2>

<div class="abs card small">
  <div class="band" style="top:21px;height:40px"></div>
  <div class="name" style="top:20px;font-size:33px">SMALL</div>
  <div class="price" style="top:59px;width:58px;height:28px;font-size:17px;line-height:28px">$49</div>
  <div class="band" style="top:87px;height:47px"></div>
  <div class="info" style="top:93px">400 VIEWER HOURS<br>(50 VIEWERS WATCHING 2 HRS-<br>4 TIMES PER MONTH)</div>
  <div class="info" style="top:147px">100 GB/MONTH OF VIDEO<br>STORAGE</div>
  <div class="more" style="left:38px;top:182px;width:109px;height:24px">More Info</div>
</div>

<div class="abs card medium">
  <div class="band" style="top:0;height:66px;border-radius:7px 7px 0 0"></div>
  <div class="name" style="top:18px;font-size:38px">MEDIUM</div>
  <div class="price" style="top:66px;width:75px;height:42px;font-size:20px;line-height:42px;border-radius:21px 0 0 21px">$399</div>
  <div class="band" style="top:116px;height:53px"></div>
  <div class="info" style="top:124px">4000 VIEWER HOURS<br>(500 VIEWERS WATCHING 2 HRS-<br>4 TIMES PER MONTH)</div>
  <div class="info" style="top:183px">500 GB/MONTH OF VIDEO<br>STORAGE</div>
  <div class="more" style="left:54px;top:218px;width:109px;height:25px">More Info</div>
</div>

<div class="abs card large">
  <div class="band" style="top:21px;height:40px"></div>
  <div class="name" style="top:20px;font-size:33px">LARGE</div>
  <div class="price" style="top:59px;width:64px;height:28px;font-size:17px;line-height:28px">$999</div>
  <div class="band" style="top:87px;height:47px"></div>
  <div class="info" style="top:92px">400 VIEWER HOURS<br>(50 VIEWERS WATCHING 2 HRS-<br>4 TIMES PER MONTH)</div>
  <div class="info" style="top:146px">2000 GB/MONTH OF VIDEO<br>STORAGE</div>
  <div class="more" style="left:40px;top:182px;width:109px;height:24px">More Info</div>
</div>

<h2 class="abs hello">HELLO THERE!</h2>
<h3 class="abs welcome">WELCOME VIREO STREAM SIMPLE</h3>
<h4 class="abs lead">LOREM IPSUM DOLAR AMET, CON SECTRTUR ADIPISC ING ELIT</h4>
<p class="abs body-copy">Our team streams services, meetings and events to viewers on any device. Plans scale with your audience, and every package includes storage for video on demand. Set up takes minutes, and our support staff help with cameras, encoders and scheduling so your broadcast runs smoothly from the first minute to the last frame.</p>

<h2 class="abs testi-title">TESTIMONIALS</h2>
<div class="abs testi" style="left:427px">
  <div class="avatar" role="img" aria-label="Portrait of a smiling client"></div>
  <div class="who">DANA REEL</div>
  <p class="quote">Clear streams and quick help every time.</p>
  <p class="quote-long">Our services reach members at home and the archive keeps every week online.</p>
</div>
<div class="abs testi" style="left:554px">
  <div class="avatar" role="img" aria-label="Portrait of a smiling client"></div>
  <div class="who">DANA REEL</div>
  <p class="quote">Setup was easy and viewers loved it.</p>
  <p class="quote-long">Staff answered each question fast and our council meetings now stream live.</p>
</div>

<section class="abs news"></section>
<div class="abs news-label">
  <svg width="16" height="12" viewBox="0 0 16 12"><rect x="0.5" y="0.5" width="15" height="11" fill="#f7a11a"/><path d="M1 1 L8 7 L15 1" stroke="#fff" stroke-width="1.2" fill="none"/></svg>
  SUBCRIBE TO OUR NEWSLETTER
</div>
<div class="abs email">YOUR EMAIL ADDRESS</div>
<div class="abs subscribe">SUBCRIBE</div>

<div class="abs brand brand-foot"><span class="brand-mark"></span>Vireo</div>
<div class="abs copy">© 2017 | PRIVACY POLICY</div>
<div class="abs social" style="left:572px"></div>
<div class="abs social" style="left:598px"></div>
<div class="abs social" style="left:624px"></div>
<div class="abs social" style="left:649px"></div>
<div class="abs to-top"><svg width="12" height="8" viewBox="0 0 12 8"><path d="M1 7 L6 2 L11 7" stroke="#fff" stroke-width="1.3" fill="none"/></svg></div>

</body>
</html>
```